i need a template design for online store

hi great designers, i need a template for any online store. But preferably well owned shopping carts. I would be an added advantage if the store is setup for me. I need a mature and attractive colours. My online store deals in electronics.

Industry/Entity Type

Shopping

Number of Pages Required

1 page

```html
<!DOCTYPE html>
<html lang="en">
<head>
<meta charset="utf-8">
<title>Volta Gear – Online Electronics Store</title>
<link rel="stylesheet" href="https://fonts.googleapis.com/css2?family=Open+Sans:wdth,wght@75..100,300..800&display=swap">
<style>
  :root {
    --brand-blue: #234a8a;
    --band-blue: rgba(36, 74, 140, 0.88);
    --accent-brown: #a27754;
    --ink-dark: #1b1f22;
    --nav-dark: rgba(10, 12, 16, 0.78);
    --text-grey: #a8adb2;
    --footer-heading: #8a96a0;
    --white: #ffffff;
    --social-grey: #55595c;
  }
  * { margin: 0; padding: 0; box-sizing: border-box; }
  html, body { width: 1200px; height: 2290px; overflow: hidden; }
  body {
    position: relative;
    background: var(--white);
    font-family: "Open Sans", Arial, sans-serif;
  }

  /* Hero */
  .hero {
    position: absolute; left: 0; top: 0; width: 1200px; height: 562px;
    background:
      radial-gradient(ellipse at 70% 35%, #6f7f92 0%, transparent 45%),
      radial-gradient(ellipse at 20% 60%, #2c5f8a 0%, transparent 50%),
      linear-gradient(160deg, #1d2734 0%, #3b4a5a 40%, #6b5240 100%);
  }
  .site-nav {
    position: absolute; left: 0; top: 0; width: 1200px; height: 75px;
    background: var(--nav-dark);
  }
  .brand {
    position: absolute; left: 77px; top: 12px;
    font-size: 36px; font-weight: 800; color: #2a5aa8; letter-spacing: 1px;
    line-height: 50px;
  }
  .nav-links {
    position: absolute; left: 312px; top: 22px;
    display: flex; list-style: none;
  }
  .nav-links li {
    color: var(--white); font-size: 20px; line-height: 28px;
    padding: 0 10px; border-left: 1px solid rgba(255,255,255,0.45);
  }
  .nav-links li:first-child { border-left: none; padding-left: 0; }
  .deals-band {
    position: absolute; left: 0; top: 188px; width: 1200px; height: 86px;
    background: var(--band-blue);
    color: var(--white); text-align: center;
    font-size: 41px; font-weight: 700; font-stretch: 75%;
    line-height: 86px;
  }
  .buy-now {
    position: absolute; left: 267px; top: 374px; width: 666px; height: 151px;
    border: 8px solid var(--accent-brown);
    color: var(--white); text-align: center;
    font-size: 106px; font-weight: 700; line-height: 132px;
  }

  /* Slider dots */
  .slider-dots { position: absolute; left: 0; top: 589px; }

  /* Products */
  .product { position: absolute; width: 486px; text-align: center; }
  .product-photo { width: 416px; height: 274px; margin: 0 auto; }
  .product-name {
    margin-top: 10px;
    font-size: 40px; font-weight: 500; color: var(--brand-blue); line-height: 48px;
  }
  .product-desc {
    margin: 14px auto 0; width: 430px;
    font-family: Verdana, "Open Sans", sans-serif;
    font-size: 16px; line-height: 20px; color: var(--text-grey);
  }
  .product-tag {
    margin-top: 14px;
    font-family: Verdana, "Open Sans", sans-serif;
    font-size: 15px; color: var(--text-grey); letter-spacing: 0.5px;
  }
  .price {
    display: inline-block; margin-top: 20px;
    width: 191px; height: 88px; border-radius: 44px;
    background: var(--brand-blue); color: var(--white);
    font-size: 70px; font-weight: 700; line-height: 86px;
  }
  .p1 { left: 111px; top: 679px; }
  .p2 { left: 597px; top: 679px; }
  .p3 { left: 111px; top: 1250px; }
  .p4 { left: 597px; top: 1250px; }
  .photo-usb { background: linear-gradient(160deg, #ffffff 20%, #2a2a2a 45%, #9a9a9a 70%, #ffffff 85%); }
  .photo-earbuds { background: linear-gradient(150deg, #3a3530 0%, #5a4f46 45%, #d98a3a 50%, #c8c8c8 60%, #3d3732 100%); }
  .photo-phone { background: linear-gradient(135deg, #c9c9cb 0%, #8e8e92 30%, #222 45%, #3b6aa0 65%, #c6c6c8 100%); }
  .photo-camera { background: radial-gradient(ellipse at 50% 55%, #1b1b1b 0%, #3a3a3a 30%, #e8e8e8 60%, #f2f2f2 100%); }

  /* Footer */
  .site-footer {
    position: absolute; left: 0; top: 1889px; width: 1200px; height: 401px;
    background: var(--ink-dark);
  }
  .footer-col { position: absolute; top: 68px; list-style: none; }
  .footer-col h3 {
    font-size: 16px; font-weight: 700; font-stretch: 75%;
    color: var(--footer-heading); letter-spacing: 0.5px; margin-bottom: 12px;
  }
  .footer-col li { color: var(--white); font-size: 16px; line-height: 33.5px; }
  .col-support { left: 139px; }
  .col-company { left: 309px; }
  .col-fun { left: 509px; }
  .col-apps { left: 698px; }
  .col-apps p { color: var(--footer-heading); font-size: 16px; line-height: 31px; }
  .col-apps p strong { color: var(--white); font-weight: 400; }
  .store-badges { position: absolute; left: 698px; top: 176px; }
  .social-links { position: absolute; left: 466px; top: 297px; }
</style>
</head>
<body>

<header class="hero" role="img" aria-label="Close-up photo of a smartwatch on a wooden desk">
  <nav class="site-nav">
    <div class="brand">VOLTA GEAR</div>
    <ul class="nav-links">
      <li>Toys and Games</li>
      <li>Electronic Gadgets</li>
      <li>Sports and Outdoors</li>
      <li>Kitchen</li>
      <li>Editors Picks</li>
    </ul>
  </nav>
  <div class="deals-band">BEST ONLINE DEALS FOR ELECTRONICS</div>
  <div class="buy-now">BUY NOW</div>
</header>

<svg class="slider-dots" width="1200" height="30" viewBox="0 0 1200 30" aria-hidden="true">
  <circle cx="525" cy="14" r="13" fill="#a27754"/>
  <circle cx="561" cy="14" r="11.5" fill="none" stroke="#a27754" stroke-width="4"/>
  <circle cx="598" cy="14" r="13" fill="#a27754"/>
  <circle cx="636" cy="14" r="13" fill="#a27754"/>
  <circle cx="674" cy="14" r="13" fill="#a27754"/>
</svg>

<main>
  <article class="product p1">
    <div class="product-photo photo-usb" role="img" aria-label="Photo of a black USB wireless adapter"></div>
    <h2 class="product-name">PRODUCT NAME HERE</h2>
    <p class="product-desc">Ne quem simul eleifend eam, alii tale probatus sea ea, cetero oportere no pri.</p>
    <p class="product-tag">SUAS NUMQUAM HONESTATIS</p>
    <div class="price">$99</div>
  </article>
  <article class="product p2">
    <div class="product-photo photo-earbuds" role="img" aria-label="Photo of a smartphone with earphones on a wooden table"></div>
    <h2 class="product-name">PRODUCT NAME HERE</h2>
    <p class="product-desc">Ne quem simul eleifend eam, alii tale probatus sea ea, cetero oportere no pri.</p>
    <p class="product-tag">SUAS NUMQUAM HONESTATIS</p>
    <div class="price">$99</div>
  </article>
  <article class="product p3">
    <div class="product-photo photo-phone" role="img" aria-label="Photo of a smartphone showing its home screen"></div>
    <h2 class="product-name">PRODUCT NAME HERE</h2>
    <p class="product-desc">Ne quem simul eleifend eam, alii tale probatus sea ea, cetero oportere no pri.</p>
    <p class="product-tag">SUAS NUMQUAM HONESTATIS</p>
    <div class="price">$99</div>
  </article>
  <article class="product p4">
    <div class="product-photo photo-camera" role="img" aria-label="Photo of a DSLR camera with strap"></div>
    <h2 class="product-name">PRODUCT NAME HERE</h2>
    <p class="product-desc">Ne quem simul eleifend eam, alii tale probatus sea ea, cetero oportere no pri.</p>
    <p class="product-tag">SUAS NUMQUAM HONESTATIS</p>
    <div class="price">$99</div>
  </article>
</main>

<footer class="site-footer">
  <ul class="footer-col col-support">
    <h3>SUPPORT</h3>
    <li>FAQ</li><li>Feedback</li><li>Contact</li><li>How It Works</li><li>Testimonials</li>
  </ul>
  <ul class="footer-col col-company">
    <h3>COMPANY</h3>
    <li>About Us</li><li>Partnership</li><li>Blog</li>
  </ul>
  <ul class="footer-col col-fun">
    <h3>FUN STUFF</h3>
    <li>Gift Certificates</li><li>Referrals</li>
  </ul>
  <div class="footer-col col-apps">
    <h3>OUR MOBILE APPS</h3>
    <p>Learn more about them <strong>HERE</strong></p>
    <p>Or, here's some handy links to download them:</p>
  </div>
  <svg class="store-badges" width="340" height="58" viewBox="0 0 340 58" aria-label="App download badges">
    <rect x="0" y="2" width="125" height="42" rx="6" fill="#2b3034"/>
    <rect x="175" y="2" width="159" height="54" rx="7" fill="#2b3034" stroke="#ffffff" stroke-width="1.5"/>
  </svg>
  <svg class="social-links" width="270" height="60" viewBox="0 0 270 60" aria-label="Social media links">
    <circle cx="29" cy="29" r="29" fill="#55595c"/>
    <circle cx="100" cy="29" r="29" fill="#55595c"/>
    <circle cx="168" cy="29" r="29" fill="#55595c"/>
    <circle cx="237" cy="29" r="29" fill="#55595c"/>
  </svg>
</footer>

</body>
</html>
```